Web Design Project

Create a web design

Target Market(s)

Upper class people interested in health

Requirements
Must have
• Templates
Nice to have
• Use the logo provided

```html
<!DOCTYPE html>
<html lang="en">
<head>
<meta charset="utf-8">
<title>Meridian Health and Fitness</title>
<link rel="stylesheet" href="https://fonts.googleapis.com/css2?family=Roboto+Condensed:wght@400;700&family=Archivo:wght@800&family=Arimo:wght@400&display=swap">
<style>
  :root {
    --green: #4f9a12;
    --blue: #1e3f92;
    --teal-tile: #2d97b0;
    --teal-frame: #d4e6e6;
    --panel-bg: #eef2f1;
    --text: #333;
    --grey-tile: #5a5d60;
    --footer: #6f9a1c;
    --yellow: #ffd21c;
    --white: #fff;
  }
  * { box-sizing: border-box; margin: 0; padding: 0; }
  html, body { width: 1200px; height: 862px; overflow: hidden; background: var(--white); }
  .page { position: relative; width: 1200px; height: 862px; font-family: "Arimo", Arial, sans-serif; color: var(--text); }
  .abs { position: absolute; }

  .brand { left: 141px; top: 28px; display: flex; align-items: center; gap: 12px; }
  .brand-mark { width: 40px; height: 40px; border-radius: 50%; background: var(--green); }
  .brand-name { font-family: "Roboto Condensed", sans-serif; font-weight: 700; font-size: 30px; color: var(--green); letter-spacing: 0.5px; text-transform: uppercase; }

  .nav { left: 141px; top: 113px; width: 918px; height: 42px; border-radius: 5px;
    background: linear-gradient(#6cc21a, #2f9a10 55%, #198f0c);
    display: flex; align-items: center; justify-content: space-between; padding: 0 10px 0 4px; }
  .nav a { font-family: "Roboto Condensed", sans-serif; font-size: 16px; color: var(--white); text-decoration: none;
    text-transform: uppercase; height: 33px; line-height: 33px; white-space: nowrap; }
  .nav a.active { background: linear-gradient(#a6dc3a, #86c522); border-radius: 4px; padding: 0 14px; }

  .badge { left: 141px; top: 165px; }
  .title-body { left: 261px; top: 174px; font-family: "Archivo", sans-serif; font-weight: 800; font-size: 44px; color: var(--blue); letter-spacing: 0.5px; }
  .title-sub { left: 262px; top: 226px; font-family: "Roboto Condensed", sans-serif; font-size: 14px; color: #555; letter-spacing: 0.3px; }

  .frame { left: 143px; top: 274px; width: 915px; height: 382px; background: #f6f6f5; border: 1px solid #ddd;
    box-shadow: 0 6px 8px -4px rgba(0,0,0,0.25); }
  .frame-border { left: 155px; top: 288px; width: 891px; height: 359px; background: var(--teal-frame); }
  .frame-inner { left: 164px; top: 297px; width: 873px; height: 341px; background: var(--panel-bg); }
  .hero-photo { left: 712px; top: 200px; width: 324px; height: 398px; border-radius: 45% 45% 12% 20%;
    background: radial-gradient(ellipse at 35% 28%, #f2c9a8 0%, #e98a5e 45%, #d9a386 72%, rgba(238,242,241,0) 100%); }

  .crunch { left: 180px; top: 308px; font-family: "Roboto Condensed", sans-serif; font-size: 23px; color: var(--blue); }
  .card { left: 178px; top: 345px; width: 526px; height: 267px; background: var(--white); border-radius: 5px; }
  .video { left: 196px; top: 370px; width: 221px; height: 164px; background: linear-gradient(160deg, #f7e3bf, #e6a85e 55%, #4a7fb4 80%, #f2d9b3); }
  .play { left: 276px; top: 427px; }
  .card-head { left: 428px; top: 379px; width: 272px; font-family: "Roboto Condensed", sans-serif; font-size: 16px; line-height: 19px; color: var(--blue); }
  .card-text { left: 428px; top: 420px; width: 274px; font-size: 12px; line-height: 19px; color: #222; }
  .shine { left: 199px; top: 532px; font-family: "Roboto Condensed", sans-serif; font-size: 16px; color: var(--blue); }
  .shine-text { left: 199px; top: 553px; font-family: "Roboto Condensed", sans-serif; font-size: 14px; color: #444; }
  .thanks { left: 199px; top: 579px; font-family: "Roboto Condensed", sans-serif; font-size: 17px; color: var(--green); }

  .tile { top: 692px; width: 212px; height: 87px; border-radius: 4px; overflow: hidden; box-shadow: 2px 3px 4px rgba(0,0,0,0.3);
    font-family: "Roboto Condensed", sans-serif; color: var(--white); text-decoration: none; }
  .tile .photo { position: absolute; top: 0; height: 87px; }
  .tile .label { position: absolute; font-size: 18px; line-height: 21px; text-transform: uppercase; text-align: right; white-space: nowrap; }
  .tile .hl { color: var(--yellow); }
  .tile svg.chev { position: absolute; right: 5px; top: 37px; }
  .tile-fitness { left: 141px; background: linear-gradient(#6cc0d4, var(--teal-tile) 50%, #1a7f98); }
  .tile-trial { left: 377px; background: linear-gradient(#ffd23c, #f4b20e); color: #5a4a1a; }
  .tile-refer { left: 613px; background: linear-gradient(#6cc0d4, var(--teal-tile) 50%, #1a7f98); }
  .tile-visit { left: 847px; background: linear-gradient(#666a6e, var(--grey-tile)); }

  .footer { left: 0; top: 816px; width: 1200px; height: 46px; background: var(--footer); }
  .copyright { left: 142px; top: 833px; font-size: 12px; color: #111; }
  .social { left: 943px; top: 825px; display: flex; gap: 11px; }
  .social span { width: 31px; height: 31px; border-radius: 50%; border: 2px solid #e9efe0; }
  .social .s1 { background: #3b5998; }
  .social .s2 { background: #2fb5e8; }
  .social .s3 { background: #e4e4e4; }
</style>
</head>
<body>
<div class="page">

  <div class="abs brand">
    <span class="brand-mark"></span>
    <span class="brand-name">Meridian Health and Fitness</span>
  </div>

  <nav class="abs nav">
    <a class="active" href="#">Home</a>
    <a href="#">Features</a>
    <a href="#">Programs &amp; Services</a>
    <a href="#">Memberships</a>
    <a href="#">Free Trials</a>
    <a href="#">News &amp; Events</a>
    <a href="#">Recruitment</a>
    <a href="#">Contact</a>
  </nav>

  <svg class="abs badge" width="106" height="106" viewBox="0 0 106 106" aria-label="12 week">
    <defs>
      <linearGradient id="badgeFill" x1="0" y1="0" x2="0" y2="1">
        <stop offset="0" stop-color="#5fd0f3"/>
        <stop offset="1" stop-color="#0d9fd8"/>
      </linearGradient>
    </defs>
    <circle cx="53" cy="53" r="52" fill="#dfe9ee"/>
    <circle cx="53" cy="53" r="48" fill="url(#badgeFill)"/>
    <g transform="rotate(-14 53 53)" fill="#fff" font-family="Roboto Condensed, sans-serif">
      <text x="24" y="56" font-size="44" font-weight="700">12</text>
      <text x="44" y="81" font-size="25">week</text>
    </g>
  </svg>
  <div class="abs title-body">BODY</div>
  <div class="abs title-sub">TRANSFORMATION</div>

  <div class="abs frame"></div>
  <div class="abs frame-border"></div>
  <div class="abs frame-inner"></div>
  <div class="abs hero-photo" role="img" aria-label="Smiling woman in an orange tank top lifting a dumbbell"></div>

  <div class="abs crunch">It’s Crunch Time!</div>
  <div class="abs card"></div>
  <div class="abs video" role="img" aria-label="Video still of women exercising on mats in a fitness class"></div>
  <svg class="abs play" width="44" height="44" viewBox="0 0 44 44" aria-label="Play video">
    <circle cx="22" cy="22" r="21" fill="#6f93d6" stroke="#dfe8f7" stroke-width="2"/>
    <path d="M16 12 L33 22 L16 32 Z" fill="#fff"/>
  </svg>
  <div class="abs card-head">12 weeks to change your body for &nbsp;the rest of your life</div>
  <p class="abs card-text">watch this video to find out about my life changing program. For less than the price of a cup of coffee &nbsp;per day. I can be your trainer it can happen!</p>
  <div class="abs shine">It’s your time to shine!</div>
  <div class="abs shine-text">The presoason will be opening on Monday 30th July, 2012, Sign up now to set up.</div>
  <div class="abs thanks">Thanks for Coming!</div>

  <a class="abs tile tile-fitness" href="#">
    <div class="photo" style="left:0;width:62px;background:linear-gradient(90deg,#f3f3f3,#e6d2c4 60%,rgba(230,210,196,0));" role="img" aria-label="Woman in white workout wear holding a towel"></div>
    <div class="label" style="right:24px;top:24px;"><span class="hl">Group Fitness</span><br>Schedule</div>
    <svg class="chev" width="14" height="16" viewBox="0 0 14 16"><path d="M1 1 L7 8 L1 15 M7 1 L13 8 L7 15" fill="none" stroke="#fff" stroke-width="2"/></svg>
  </a>

  <a class="abs tile tile-trial" href="#">
    <div class="photo" style="left:0;width:100px;background:linear-gradient(90deg,#c98a64,#d84a3c 55%,rgba(244,178,14,0));" role="img" aria-label="Woman doing crunches on an exercise ball"></div>
    <div class="label" style="right:30px;top:24px;">Try Us<br>Free Today</div>
    <svg class="chev" width="14" height="16" viewBox="0 0 14 16"><path d="M1 1 L7 8 L1 15 M7 1 L13 8 L7 15" fill="none" stroke="#5a4a1a" stroke-width="2"/></svg>
  </a>

  <a class="abs tile tile-refer" href="#">
    <div class="photo" style="left:0;width:63px;background:linear-gradient(#8a7a68,#3a3a3e);" role="img" aria-label="Portrait of a young man in a dark suit"></div>
    <div class="label" style="right:22px;top:34px;">Refer a <span class="hl">Friend</span></div>
    <svg class="chev" width="14" height="16" viewBox="0 0 14 16"><path d="M1 1 L7 8 L1 15 M7 1 L13 8 L7 15" fill="none" stroke="#fff" stroke-width="2"/></svg>
  </a>

  <a class="abs tile tile-visit" href="#">
    <div class="label" style="left:10px;top:14px;font-size:17px;line-height:20px;text-align:left;">Come and<br>check us<br>out</div>
    <div class="photo" style="right:0;width:76px;background:linear-gradient(90deg,#2a2a2a,#8c8c8c 40%,#d8b8a0 60%,#444);" role="img" aria-label="Woman lifting a dumbbell in a gym"></div>
  </a>

  <div class="abs footer"></div>
  <div class="abs copyright">© 2012. Meridian PT. All Rights Reserved</div>
  <div class="abs social" aria-label="Social links">
    <span class="s1"></span>
    <span class="s2"></span>
    <span class="s3"></span>
  </div>

</div>
</body>
</html>
```